Gymnastics Award Design Needed--for kids

Need a gymnastics certificate or award designed. Will be printed on a piece of 8.5x11 paper. The award will be celebrating the gymnast learning a new skill in gymnastics. So it should be fun, but still look "official". Needs to look good hanging on a gymnast's bedroom wall.

It should say "The Aerial Cartwheel Club"
I will be using this design to change it based on the skill.

My main colors are:
#34475D
#E1467A
#7555A4

So should use those, but can add others

My website is tumblenestpro.com so you can see the look/feel.

Target Market(s)

Main audience will be girls ages 5-12, but will also be used by slightly older girls and boys. So needs to be fun, not too gender specific.

Industry/Entity Type

Learning

Requirements
Must have
• The following will need to go on the certificate:
• * Name of Skill
• * Image of Skill
• * Gymnast's Name
• * my logo
• * Gym's Logo
• * Gym's Name
• Optional: Date

```html
<!DOCTYPE html>
<html lang="en">
<head>
<meta charset="utf-8">
<title>The Aerial Cartwheel Club – Certificate</title>
<link href="https://fonts.googleapis.com/css2?family=Luckiest+Guy&family=Great+Vibes&family=Open+Sans:wght@400;600&display=swap" rel="stylesheet">
<style>
  :root {
    --navy: #34475D;
    --pink: #E1467A;
    --purple: #7555A4;
    --yellow: #F2E62E;
    --teal: #17AFA3;
    --paper: #FFFFFF;
    --ink: #222222;
    --silhouette: #D6D6D6;
    --dots: #3B6FB6;
  }
  html, body { margin: 0; padding: 0; overflow: hidden; background: #EDEDED; }
  .certificate {
    position: relative;
    width: 1200px;
    height: 940px;
    background: var(--paper);
    font-family: "Open Sans", sans-serif;
    color: var(--ink);
    overflow: hidden;
  }
  .certificate-art { position: absolute; inset: 0; }
  .cloud { filter: drop-shadow(0 4px 6px rgba(0,0,0,0.25)); }
  .skill-title {
    font-family: "Luckiest Guy", sans-serif;
    font-size: 40px;
    fill: var(--navy);
    stroke: var(--yellow);
    stroke-width: 5px;
    paint-order: stroke fill;
  }
  .text-block { position: absolute; left: 0; width: 1200px; text-align: center; margin: 0; }
  .presented-to { top: 408px; font-size: 22px; font-weight: 600; letter-spacing: 0.5px; line-height: 30px; }
  .gymnast-name {
    top: 462px; font-family: "Great Vibes", cursive; font-size: 66px;
    color: var(--purple); line-height: 76px;
  }
  .recognition { top: 550px; font-size: 21px; letter-spacing: 2.5px; line-height: 40px; }
  .brand-mark {
    position: absolute; left: 200px; top: 686px; width: 225px;
    display: flex; align-items: center; gap: 8px;
    font-size: 18px; line-height: 28px; color: var(--pink); letter-spacing: 0.5px; white-space: nowrap;
  }
  .brand-dot { width: 20px; height: 20px; border-radius: 50%; background: var(--purple); flex: none; }
  .sign-field { position: absolute; top: 716px; width: 198px; text-align: center; }
  .sign-field .line { border-top: 3px dotted var(--dots); }
  .sign-field .label { font-size: 20px; font-weight: 600; margin-top: 4px; line-height: 28px; }
  .field-signature { left: 438px; }
  .field-date { left: 662px; }
  .gym-mark {
    position: absolute; left: 870px; top: 622px; width: 124px;
    display: flex; flex-direction: column; align-items: center; gap: 8px;
    font-size: 16px; font-weight: 600; color: var(--pink); text-align: center; line-height: 20px;
  }
  .gym-circle { width: 84px; height: 84px; border-radius: 50%; background: var(--navy); }
</style>
</head>
<body>
<main class="certificate">
  <svg class="certificate-art" viewBox="0 0 1200 940" width="1200" height="940">
    <defs>
      <clipPath id="inner-area"><rect x="31" y="29" width="1144" height="876"/></clipPath>
      <path id="title-arc" d="M 250 300 Q 592 50 934 300"/>
    </defs>

    <g class="bubble-field" clip-path="url(#inner-area)">
      <rect x="0" y="0" width="1200" height="940" fill="var(--navy)"/>
      <circle cx="62" cy="139" r="115" fill="var(--pink)"/>
      <circle cx="532" cy="62" r="110" fill="var(--teal)"/>
      <circle cx="259" cy="101" r="115" fill="var(--purple)"/>
      <circle cx="420" cy="126" r="115" fill="var(--yellow)"/>
      <circle cx="700" cy="70" r="110" fill="var(--pink)"/>
      <circle cx="1113" cy="62" r="115" fill="var(--teal)"/>
      <circle cx="940" cy="126" r="115" fill="var(--yellow)"/>
      <circle cx="1076" cy="217" r="110" fill="var(--purple)"/>
      <circle cx="1138" cy="333" r="110" fill="var(--pink)"/>
      <circle cx="1113" cy="539" r="110" fill="var(--purple)"/>
      <circle cx="1170" cy="650" r="90" fill="var(--teal)"/>
      <circle cx="1089" cy="771" r="120" fill="var(--yellow)"/>
      <circle cx="965" cy="849" r="120" fill="var(--pink)"/>
      <circle cx="804" cy="836" r="100" fill="var(--purple)"/>
      <circle cx="717" cy="860" r="120" fill="var(--yellow)"/>
      <circle cx="482" cy="823" r="100" fill="var(--pink)"/>
      <circle cx="383" cy="836" r="100" fill="var(--teal)"/>
      <circle cx="334" cy="890" r="120" fill="var(--yellow)"/>
      <circle cx="74" cy="539" r="110" fill="var(--teal)"/>
      <circle cx="49" cy="436" r="110" fill="var(--pink)"/>
      <circle cx="87" cy="320" r="110" fill="var(--purple)"/>
      <circle cx="148" cy="178" r="120" fill="var(--yellow)"/>
      <circle cx="124" cy="746" r="130" fill="var(--yellow)"/>
    </g>

    <rect x="23" y="21" width="1160" height="892" fill="none" stroke="var(--navy)" stroke-width="5"/>
    <rect x="31" y="29" width="1144" height="876" fill="none" stroke="var(--paper)" stroke-width="6"/>

    <g class="cloud" fill="var(--paper)">
      <ellipse cx="600" cy="470" rx="470" ry="310"/>
      <circle cx="240" cy="240" r="140"/>
      <circle cx="420" cy="195" r="130"/>
      <circle cx="600" cy="175" r="130"/>
      <circle cx="790" cy="185" r="130"/>
      <circle cx="955" cy="235" r="140"/>
      <circle cx="1050" cy="370" r="110"/>
      <circle cx="1060" cy="520" r="100"/>
      <circle cx="1030" cy="670" r="110"/>
      <circle cx="890" cy="755" r="115"/>
      <circle cx="720" cy="790" r="105"/>
      <circle cx="540" cy="790" r="105"/>
      <circle cx="365" cy="755" r="115"/>
      <circle cx="205" cy="675" r="115"/>
      <circle cx="165" cy="520" r="100"/>
      <circle cx="160" cy="370" r="110"/>
    </g>

    <text class="skill-title" text-anchor="middle">
      <textPath href="#title-arc" startOffset="50%" textLength="600" lengthAdjust="spacingAndGlyphs">THE AERIAL CARTWHEEL CLUB</textPath>
    </text>

    <rect role="img" aria-label="Illustration of a gymnast performing a split leap" x="476" y="236" width="266" height="125" rx="60" fill="#F4C7B5"/>
    <rect role="img" aria-label="Faint grey silhouette of a leaping gymnast" x="150" y="350" width="145" height="188" rx="30" fill="var(--silhouette)" opacity="0.6"/>
    <rect role="img" aria-label="Faint grey silhouette of a leaping gymnast" x="886" y="350" width="145" height="188" rx="30" fill="var(--silhouette)" opacity="0.6"/>
  </svg>

  <p class="text-block presented-to">PRESENTED TO</p>
  <p class="text-block gymnast-name">Maya Brookfield</p>
  <p class="text-block recognition">IN RECOGNITION OF OUTSTANDING EFFORT<br>AND ATTENDENCE IN BALLET CLASS</p>

  <div class="brand-mark"><span class="brand-dot"></span><span>TUMBLENEST PRO</span></div>

  <div class="sign-field field-signature"><div class="line"></div><div class="label">SIGNATURE</div></div>
  <div class="sign-field field-date"><div class="line"></div><div class="label">DATE</div></div>

  <div class="gym-mark"><span class="gym-circle"></span><span>SPRINGLINE GYM</span></div>
</main>
</body>
</html>
```